Homepage layout for online ad network

Attached is our Calvrex Media logo and updated brief (I can't seem to delete the old logo and brief, but they're no longer relevant).

This project was originally posted with a different logo and corporate name, but we have decided to stay with our current logo and name and redesign the site.

Your design is for a homepage only - design, no coding (I'll get someone else to take your PSD and code it).

Your homepage will make use of a Flash slider - BUT YOU ARE NOT REQUIRED TO PROVIDE THE FLASH. Instead, simply provide the layout and at least two static examples out of the four different sections that will eventually be in the slider.

Much of this design is based on the design of a competitor (listed in the brief).

Please ask whatever questions you need to in order to clarify instructions.
Updates

Project updated to include new logo (and correspondingly new color scheme).

Brief changed slightly.

Thank you for submitting designs for this project in the past.

After some internal strategy work, we have decided to retain our initial corporate identity, Calvrex Media.

If you have submitted a design for the original brief and are available, please re-work your best prior design to reflect the color scheme in the newly uploaded logo.

Target Market(s)

This site is aimed primarily at young professionals who buy digital media on behalf of large advertisers.

Industry/Entity Type

Media

Requirements
Must have
• modern white space
Should not have
• no Flash outside of slider

```html
<!DOCTYPE html>
<html lang="en">
<head>
<meta charset="utf-8">
<title>Calvrex Media</title>
<link rel="stylesheet" href="https://fonts.googleapis.com/css2?family=Source+Sans+3:wght@400;600&display=swap">
<style>
:root{
  --cream:#fdf8e6;
  --cream-light:#fffdf6;
  --charcoal:#333333;
  --charcoal-dark:#262626;
  --red:#e21d26;
  --red-dark:#b51e2a;
  --red-panel:#a9202c;
  --white:#ffffff;
  --ink:#2b2b2b;
}
*{margin:0;padding:0;box-sizing:border-box}
html,body{width:1200px;height:900px;overflow:hidden}
body{
  position:relative;
  font-family:"Source Sans 3",sans-serif;
  background:linear-gradient(180deg,var(--cream) 0%,var(--cream) 45%,var(--cream-light) 100%);
  color:var(--ink);
}
a{text-decoration:none}
.brand{position:absolute;left:239px;top:30px;display:flex;align-items:center;gap:14px}
.brand-mark{width:40px;height:40px;background:var(--red)}
.brand-name{
  font-size:29px;font-weight:400;letter-spacing:6px;line-height:28px;color:var(--red);
}

.main-nav{
  position:absolute;left:0;top:117px;width:1200px;height:33px;
  background:var(--charcoal);border-top:2px solid var(--white);
}
.main-nav a{
  position:absolute;top:0;height:31px;line-height:31px;text-align:center;
  color:var(--white);font-size:20px;
  border-right:2px solid var(--red-dark);
}
.main-nav a.active{background:linear-gradient(180deg,var(--red),var(--red-dark))}

.slider{position:absolute;left:0;top:150px;width:1200px;height:234px;
  background:linear-gradient(90deg,#d91c25,var(--red) 50%,#d91c25)}
.slide-text{position:absolute;left:220px;top:0;width:272px;height:234px;
  background:var(--red-panel);border-left:3px solid var(--charcoal);color:var(--white)}
.slide-title{position:absolute;left:18px;top:24px;font-size:37px;font-weight:600;letter-spacing:-1px;white-space:nowrap}
.slide-body{position:absolute;left:30px;top:100px;font-size:23px;line-height:31px;white-space:nowrap}
.slide-link{position:absolute;right:30px;top:206px;font-size:15px;color:var(--white)}
.slide-photo{position:absolute;left:492px;top:0;width:484px;height:234px;
  background:linear-gradient(135deg,#e8e0d0 0%,#b89a72 40%,#4d3a2b 70%,#c9412c 100%);
  border-right:3px solid var(--charcoal)}

.slider-controls{position:absolute;left:0;top:384px;width:1200px;height:34px;background:var(--charcoal)}
.slider-controls svg{position:absolute;top:5px}
.dot{position:absolute;top:11px;width:14px;height:13px;background:var(--cream)}
.dot.active{background:var(--red)}

.section-tile{position:absolute;width:160px;text-align:center}
.tile-image{display:block;width:160px;height:102px;border:4px solid #111;border-radius:14px}
.tile-label{display:block;margin-top:10px;font-size:20px;color:var(--ink)}

.news{position:absolute;left:664px;top:451px;width:312px;height:315px;border-radius:14px;
  overflow:hidden;background:linear-gradient(180deg,var(--charcoal-dark),#3a3a3a 60%,var(--charcoal-dark))}
.news-title{height:42px;padding:8px 0 0 24px;font-size:24px;font-weight:400;color:var(--white);
  background:linear-gradient(180deg,var(--red),#c81c25)}
.news-item{position:absolute;left:24px;width:272px;font-size:13px;font-weight:400;line-height:17.5px;color:var(--white);letter-spacing:-0.3px}
.news-rule{position:absolute;left:52px;width:202px;height:1px;background:#777}

.footer-rule{position:absolute;left:122px;top:816px;width:954px;height:4px;background:var(--charcoal-dark)}
.footer-nav{position:absolute;left:0;top:835px;width:1200px;text-align:center}
.footer-nav a{margin:0 15px;font-size:17px;color:var(--red);letter-spacing:-0.3px}
</style>
</head>
<body>
<header class="brand">
  <span class="brand-mark"></span>
  <div class="brand-name">CALVREX<br>MEDIA</div>
</header>

<nav class="main-nav">
  <a class="active" href="#" style="left:528px;width:110px">Beauty</a>
  <a href="#" style="left:638px;width:124px">Cooking</a>
  <a href="#" style="left:762px;width:129px">Parenting</a>
  <a href="#" style="left:891px;width:85px">Video</a>
</nav>

<section class="slider">
  <div class="slide-text">
    <h1 class="slide-title">Cooking Media</h1>
    <p class="slide-body">Lorem ipsum appareat<br>phaedrum nam ne.</p>
    <a class="slide-link" href="#">Learn More</a>
  </div>
  <div class="slide-photo" role="img" aria-label="Plated dish of grilled eggplant, mozzarella, tomato and fresh herbs"></div>
</section>

<div class="slider-controls">
  <svg style="left:239px" width="36" height="24" viewBox="0 0 36 24"><path d="M34 12H4M14 2L4 12l10 10" fill="none" stroke="#fff" stroke-width="4"/></svg>
  <span class="dot active" style="left:520px"></span>
  <span class="dot" style="left:563px"></span>
  <span class="dot" style="left:608px"></span>
  <span class="dot" style="left:652px"></span>
  <svg style="left:911px" width="36" height="24" viewBox="0 0 36 24"><path d="M2 12h30M22 2l10 10-10 10" fill="none" stroke="#fff" stroke-width="4"/></svg>
</div>

<a class="section-tile" href="#" style="left:260px;top:455px">
  <span class="tile-image" role="img" aria-label="Close-up of a made-up eye" style="background:linear-gradient(135deg,#c9a27e,#8a5e3c 55%,#d9b894)"></span>
  <span class="tile-label">Beauty</span>
</a>
<a class="section-tile" href="#" style="left:454px;top:455px">
  <span class="tile-image" role="img" aria-label="Bowl of green salad with croutons" style="background:linear-gradient(135deg,#2f4a1e,#8bbf3c 50%,#d6c46a)"></span>
  <span class="tile-label">Cooking</span>
</a>
<a class="section-tile" href="#" style="left:260px;top:637px">
  <span class="tile-image" role="img" aria-label="Black and white photo of baby feet in a parent's hands" style="background:linear-gradient(135deg,#e6e6e6,#9a9a9a 55%,#5a5a5a)"></span>
  <span class="tile-label">Parenting</span>
</a>
<a class="section-tile" href="#" style="left:454px;top:637px">
  <span class="tile-image" role="img" aria-label="Film clapperboard" style="background:linear-gradient(180deg,#f2f2f2,#8a8a8a 40%,#555)"></span>
  <span class="tile-label">Video</span>
</a>

<aside class="news">
  <h2 class="news-title">News</h2>
  <p class="news-item" style="top:66px">Lorem ipsum pertinax forensibus scriptorem ad cum, duo no alii possit. Ad populo adversarium ius, aliquip scripta in mei, ut odio repudiare pri.</p>
  <span class="news-rule" style="top:127px"></span>
  <p class="news-item" style="top:151px">Lorem ipsum pertinax forensibus scriptorem ad cum, duo no alii possit. Ad populo adversarium ius, aliquip scripta in mei, ut odio repudiare pri.</p>
  <span class="news-rule" style="top:213px"></span>
  <p class="news-item" style="top:239px">Lorem ipsum pertinax forensibus scriptorem ad cum, duo no alii possit. Ad populo adversarium ius, aliquip scripta in mei, ut odio repudiare pri.</p>
</aside>

<div class="footer-rule"></div>
<nav class="footer-nav">
  <a href="#">About Us</a>
  <a href="#">Contact Us</a>
  <a href="#">Management Team</a>
  <a href="#">News</a>
  <a href="#">Careers</a>
</nav>
</body>
</html>
```